Salmon Shop that sells both wholesale and retail salmon in a variety of ways.

"Harbour Fillet Co" is a business that is selling atlantic salmon in every way possible. We will be a salmon butcher to the public for retail purchase and we will also be out and about trying to sell our products to restaurants cafes and any other wholesale way. Our product is from Tasmania but we will be trading on the Sunshine Coast. The shop design has an urban, rustic feel and very much about the product. One of the owners has worked on salmon farms for 15 years and we want it to be very specialised and quality. I have nothing to offer you to help with this design....I would like both a salmon on the card, not sure if image or silohette is best and would like the other side to have a fillet with a tag of some sort. We are looking for a logo also. Use a photo of an Atlantic Salmon, Atlantic Salmon have two fins along the back.
Updates

Project Deadline Extended Reason: I am extending the deadline as I have still not got exactly what I want. All designers have added something great to what I am after and I just need someone to pull it all together. I have put in a new brief with a sketched image to help so we can get this perfect. Please read all the instructions. Thank you Added Monday, February 16, 2015

Target Market(s)

Restaurants, cafes

Industry/Entity Type

Retail

Contact Information for Business Card

Harbour Fillet Co (Not to have "Shop" at the end.Shop 12/130-164 Brisbane RdMooloolaba 4557

Colors
1c66ab

Requirements
Must have
• logo for harbour fillet Co with the S being salmon fillet of fresh salmon on white platemap of tasmaniasepia /black and white image of atlantic salmon
Nice to have
• fillet of salmonmap of tasmaniasalmon
Should not have
• Not Shop at the end.

```html
<!DOCTYPE html>
<html lang="en">
<head>
<meta charset="utf-8">
<title>Harbour Fillet Co — Business Card</title>
<link rel="stylesheet" href="https://fonts.googleapis.com/css2?family=Oswald:wght@500&family=Open+Sans:wght@400;700&display=swap">
<style>
  :root {
    --salmon: #f38a6c;
    --ink: #111111;
    --paper: #ffffff;
    --backdrop: #ece7e1;
    --text: #1a1a1a;
  }
  * { box-sizing: border-box; margin: 0; padding: 0; }
  html, body {
    width: 1200px;
    height: 1200px;
    overflow: hidden;
    background: var(--backdrop);
  }
  .canvas {
    position: relative;
    width: 1200px;
    height: 1200px;
  }
  .card {
    position: absolute;
    box-shadow: 0 3px 8px rgba(0, 0, 0, 0.18);
  }
  .card-front {
    left: 272px;
    top: 231px;
    width: 621px;
    height: 380px;
    background: var(--salmon);
  }
  .front-frame {
    position: absolute;
    inset: 19px 21px 21px 21px;
    border: 2px solid var(--paper);
  }
  .front-name {
    position: absolute;
    left: 0;
    right: 0;
    top: 50%;
    transform: translateY(-50%);
    text-align: center;
    font-family: "Oswald", sans-serif;
    font-weight: 500;
    font-size: 40px;
    line-height: 1.1;
    letter-spacing: 1px;
    text-transform: uppercase;
    color: var(--ink);
  }
  .card-back {
    left: 283px;
    top: 637px;
    width: 610px;
    height: 372px;
    display: flex;
    background: var(--paper);
  }
  .back-brand-panel {
    position: relative;
    width: 289px;
    height: 100%;
    background: var(--salmon);
  }
  .brand-ring {
    position: absolute;
    left: 60px;
    top: 106px;
    width: 168px;
    height: 168px;
    border: 3px solid var(--paper);
    border-radius: 50%;
    display: flex;
    align-items: center;
    justify-content: center;
    text-align: center;
  }
  .brand-ring-name {
    font-family: "Oswald", sans-serif;
    font-weight: 500;
    font-size: 24px;
    line-height: 1.15;
    letter-spacing: 0.5px;
    text-transform: uppercase;
    color: var(--paper);
  }
  .back-contact {
    position: relative;
    flex: 1;
    padding: 156px 0 0 25px;
    font-family: "Open Sans", sans-serif;
    color: var(--text);
  }
  .contact-label {
    display: flex;
    align-items: center;
    gap: 5px;
    font-size: 12px;
    font-weight: 700;
    text-transform: uppercase;
  }
  .pin-icon { width: 11px; height: 15px; }
  .contact-address {
    margin: 4px 0 0 15px;
    font-size: 12.5px;
    line-height: 1.4;
    font-style: normal;
  }
</style>
</head>
<body>
  <main class="canvas">
    <section class="card card-front" aria-label="Business card front">
      <div class="front-frame"></div>
      <p class="front-name">Harbour<br>Fillet Co</p>
    </section>

    <section class="card card-back" aria-label="Business card back">
      <div class="back-brand-panel">
        <div class="brand-ring">
          <p class="brand-ring-name">Harbour<br>Fillet Co</p>
        </div>
      </div>
      <div class="back-contact">
        <p class="contact-label">
          <svg class="pin-icon" viewBox="0 0 11 15" aria-hidden="true">
            <path d="M5.5 0C2.5 0 0 2.4 0 5.4 0 9.4 5.5 15 5.5 15S11 9.4 11 5.4C11 2.4 8.5 0 5.5 0Zm0 7.6a2.2 2.2 0 1 1 0-4.4 2.2 2.2 0 0 1 0 4.4Z" fill="#111"/>
          </svg>
          Shop:
        </p>
        <address class="contact-address">
          7/210-236 WATTLEBAY Rd,<br>
          KIRRAWEE 4812
        </address>
      </div>
    </section>
  </main>
</body>
</html>
```